Children's Book Illustration

Looking for an illustrator for a children's book. The book is for ages 4 to 8 and tells a story about a young boy going to fly a kite and the effects it has on his neighborhood. I like Milo Fenwick's work and will a prefer colorful, whimsical look. This book will require about 10 page spreads of illustration. I'll need to see at least three to decide how to award the project.
Project Deadline Extended
Reason: This is our first project with SketchHarbor so I'm not sure how the process works. I have a specific question that I'm trying to ask of Customer Support. In the meantime, I'm extending the deadline just to make sure the project doesn't expire before we want it to.
Target Market(s)
Preschool children and teachers
Industry/Entity Type
Work
Look and feel

```html
<!DOCTYPE html>
<html lang="en">
<head>
<meta charset="utf-8">
<title>Purple Dragon Kite – Spread</title>
<link href="https://fonts.googleapis.com/css2?family=Noto+Sans:wght@400;600&display=swap" rel="stylesheet">
<style>
  :root {
    --sky-top: #45ace5;
    --sky-mid: #8cc6ec;
    --sky-low: #d2e5f3;
    --gutter: #8e969c;
    --hill: #3f9a3a;
    --hill-light: #56b14a;
    --ground: #4a3b1c;
    --ink: #111111;
    --figure-warm: #c9a07a;
    --figure-cool: #b9a6d6;
  }
  * { margin: 0; padding: 0; box-sizing: border-box; }
  html, body { width: 1200px; height: 900px; overflow: hidden; }
  body { position: relative; background: var(--sky-low); color: var(--ink); }

  .page { position: absolute; top: 0; height: 900px; overflow: hidden; }
  .page--left {
    left: 0; width: 590px;
    background: linear-gradient(to bottom, var(--sky-top) 0%, var(--sky-mid) 45%, var(--sky-low) 80%);
    font-family: "Noto Sans", sans-serif; font-weight: 600; font-size: 14.5px; line-height: 18px;
  }
  .page--right {
    left: 597px; width: 603px;
    background: linear-gradient(to bottom, var(--sky-top) 0%, var(--sky-mid) 50%, var(--sky-low) 78%);
    font-family: "Noto Sans", sans-serif; font-weight: 400; font-size: 16px; line-height: 20px;
  }
  .gutter { position: absolute; left: 590px; top: 0; width: 7px; height: 900px;
    background: linear-gradient(to right, #b8bec3, var(--gutter), #c4c9cd); }

  .para { position: absolute; white-space: nowrap; }
  .page--left .para { left: 51px; text-indent: 13px; }
  .page--right .para { left: 50px; text-indent: 14px; }

  .scene { position: absolute; display: block; }
  .scene--hill { left: 0; top: 630px; }
  .scene--ground { left: 0; top: 703px; width: 603px; height: 197px; background: var(--ground); }
</style>
</head>
<body>
  <section class="page page--left">
    <p class="para" style="top:48px">So Toby, Mrs. Reyes, Mr. Mason, Molly and Grace walked<br>down the street.</p>
    <p class="para" style="top:109px;left:68px;text-indent:0">Mr. and Mrs. Chen were gardening as they passed by<br>&ldquo;What&rsquo;s going on, Toby?&rdquo; Mr. Chen asked.</p>
    <p class="para" style="top:165px;text-indent:9px">&ldquo;My big brother said the perfect thing for me to do is to<br>go fly a kite. We&rsquo;re on our way to find out what he meant.&rdquo;</p>
    <p class="para" style="top:223px;left:52px">Mr. Chen looked up at the beautiful blue sky and the<br>white puffy clouds.</p>
    <p class="para" style="top:270px;left:50px">&ldquo;I believe your brother thought that today was a perfect<br>day to sit and watch a purple dragon kite flying high in the<br>clouds. We sure could use a break from gardening. May we<br>come along?&rdquo;</p>
    <p class="para" style="top:367px">&ldquo;Sure, Mr. Chen&rdquo;, Toby said.</p>
    <p class="para" style="top:403px">&ldquo;I&rsquo;ll get the lawn chairs&rdquo;, Mrs. Chen said.</p>
    <p class="para" style="top:440px;left:53px">Soon Toby and all his neighbors reached the vacant lot.<br>Mr. and Mrs. Chen got settled in their lawn chairs. Mr. Mason<br>helped Toby with the kite string.</p>
    <p class="para" style="top:528px;left:52px">Molly and Grace were helping Mrs. Reyes serve chocolate<br>chip cookies to everyone.</p>

    <svg class="scene scene--hill" width="590" height="270" viewBox="0 0 590 270">
      <path d="M0 150 Q 200 70 420 95 Q 530 105 590 125 L590 270 L0 270 Z" fill="var(--hill)"/>
      <path d="M0 150 Q 200 70 420 95 Q 530 105 590 125 L590 140 Q 420 110 240 120 Q 100 130 0 175 Z" fill="var(--hill-light)" opacity="0.5"/>
      <rect x="40" y="10" width="500" height="245" rx="30" fill="var(--figure-cool)" opacity="0.55"
            role="img" aria-label="Illustration: Toby holding the kite string beside Mr. Mason, with Mr. and Mrs. Chen in lawn chairs, Molly and Grace, and Mrs. Reyes serving cookies on a grassy hill"/>
    </svg>
  </section>

  <div class="gutter"></div>

  <section class="page page--right">
    <p class="para" style="top:48px">Back at Toby&rsquo;s house, Toby&rsquo;s mother was leaving for<br>the mall.&nbsp; She was looking for Toby.&nbsp; She looked in Toby&rsquo;s<br>bedroom.&nbsp; She looked in the kitchen.&nbsp; She looked in the<br>basement.&nbsp; Finally, she looked in the garage and found Toby&rsquo;s<br>dad but no Toby.</p>
    <p class="para" style="top:168px">&ldquo;Have you seen Toby?&rdquo; she asked.&nbsp; &ldquo;I&rsquo;m on my way to the<br>mall and thought he might like to go.&rdquo;</p>
    <p class="para" style="top:228px">&ldquo;Yes, he was here earlier.&nbsp; I think he&rsquo;s in the backyard with<br>Owen.&rdquo;</p>
    <p class="para" style="top:288px">Toby&rsquo;s mom and dad found Owen in the backyard still<br>practicing baseball but no Toby.</p>
    <p class="para" style="top:348px">&ldquo;Have you seen Toby?&rdquo; his mother asked Owen.</p>
    <p class="para" style="top:388px">&ldquo;He was here a while ago but I don&rsquo;t know where he went.&rdquo;</p>
    <p class="para" style="top:428px">&ldquo;I&rsquo;m worried about Toby,&rdquo; his mother said.&nbsp; &ldquo;He told me<br>earlier that he was doing something for Owen and would be<br>right back.&nbsp; I&rsquo;ve looked everywhere and I can&rsquo;t find him.&nbsp; He&rsquo;s<br>not in the house.&nbsp; He&rsquo;s not in the garage.&nbsp; He&rsquo;s not out here<br>with you.&rdquo;</p>
    <p class="para" style="top:548px">&ldquo;Toby! Toby! Toby!&rdquo; called his parents and Owen as they<br>began to search for Toby.</p>
    <p class="para" style="top:608px">Suddenly, Owen looked up and saw the purple dragon kite<br>flying high in the sky.</p>
    <p class="para" style="top:668px;left:54px">&ldquo;I think I know where Toby might be.&nbsp; Follow me,&rdquo; Owen said.</p>

    <div class="scene scene--ground">
      <svg width="603" height="197" viewBox="0 0 603 197">
        <rect x="55" y="12" width="475" height="185" rx="24" fill="var(--figure-warm)" opacity="0.45"
              role="img" aria-label="Illustration: Toby's dad, Owen and Toby's mom looking worried as they wonder where Toby has gone"/>
      </svg>
    </div>
  </section>
</body>
</html>
```